Sports Therapy and Personal Training

I need a business card design for a new business based in Toronto called "Vellmore Athletics" I am a sports therapist as well as a strength and conditioning coach, therefore I work mainly with high level athletes and physically active people. I am starting my own therapy/training business. The services I will be offering include fitness consultation, personal training, athlete assessments, and rehabilitation therapy. These services will be delivered in peoples homes and/or a facility in which I rent space.

The final design should communicate "high-end" and "quality"

Target Market(s)

athletes and physically active people

Industry/Entity Type

Fitness

Requirements
Must have
• 1. The business logo - files attached

2. my name and credentials

Derek Vellmore - CAT(C), CK, CSCS,

Certified Athletic Therapist
Strength and Conditioning Specialist

3. website - www.vellmoreathletics.example

4. email address - derek@vellmoreathletics.example

5. phone number

```html
<!DOCTYPE html>
<html lang="en">
<head>
<meta charset="utf-8">
<title>Vellmore Athletics – Business Card</title>
<link rel="stylesheet" href="https://fonts.googleapis.com/css2?family=Source+Sans+3:ital,wght@0,400;0,700;1,400&display=swap">
<style>
  :root {
    --page-bg: #ffffff;
    --card-bg-top: #e3e3e3;
    --card-bg-bottom: #dadada;
    --accent-red: #e8202a;
    --text-dark: #3f3f3f;
    --text-italic: #6a5844;
    --wave-light: #f3f3f3;
    --wave-mid: #e6e6e6;
    --wave-dark: #d6d6d6;
  }
  * { margin: 0; padding: 0; box-sizing: border-box; }
  html, body {
    width: 1200px;
    height: 900px;
    overflow: hidden;
    background: var(--page-bg);
    font-family: "Source Sans 3", "Myriad Pro", sans-serif;
  }
  .canvas {
    position: relative;
    width: 1200px;
    height: 900px;
  }
  .card {
    position: absolute;
    top: 94px;
    width: 410px;
    height: 716px;
    background: linear-gradient(180deg, var(--card-bg-top), var(--card-bg-bottom));
    overflow: hidden;
  }
  .card--front { left: 120px; }
  .card--back { left: 670px; }

  .corner {
    position: absolute;
    width: 66px;
    height: 66px;
    background: var(--accent-red);
    z-index: 2;
  }
  .corner--top-left { top: 0; left: 0; clip-path: polygon(0 0, 100% 0, 0 100%); }
  .corner--bottom-right { bottom: 0; right: 0; clip-path: polygon(100% 0, 100% 100%, 0 100%); }

  .wave {
    position: absolute;
    left: 0;
    bottom: 0;
    width: 410px;
    height: 170px;
  }

  .brand {
    position: absolute;
    left: 0;
    right: 0;
    top: 296px;
    display: flex;
    justify-content: center;
    align-items: center;
    gap: 12px;
  }
  .brand__mark {
    width: 16px;
    height: 16px;
    background: var(--accent-red);
  }
  .brand__name {
    font-size: 32px;
    font-weight: 700;
    color: var(--text-dark);
    letter-spacing: 0.5px;
  }

  .person {
    position: absolute;
    right: 20px;
    top: 98px;
    text-align: right;
  }
  .person__name {
    font-size: 19px;
    color: var(--text-dark);
    margin-bottom: 16px;
  }
  .person__title {
    font-size: 14px;
    font-style: italic;
    color: var(--text-italic);
    line-height: 25px;
  }

  .contact {
    position: absolute;
    left: 20px;
    top: 452px;
    list-style: none;
    font-size: 15px;
    color: var(--text-dark);
    line-height: 23px;
  }
</style>
</head>
<body>
<main class="canvas">
  <section class="card card--front">
    <div class="corner corner--top-left"></div>
    <div class="brand">
      <span class="brand__mark"></span>
      <span class="brand__name">Vellmore Athletics</span>
    </div>
    <svg class="wave" viewBox="0 0 410 170" role="img" aria-label="Soft dotted halftone wave texture along the bottom of the card">
      <defs>
        <linearGradient id="waveFrontFill" x1="0" y1="0" x2="0" y2="1">
          <stop offset="0" stop-color="var(--wave-light)"/>
          <stop offset="0.45" stop-color="var(--wave-mid)"/>
          <stop offset="1" stop-color="var(--wave-dark)"/>
        </linearGradient>
      </defs>
      <path d="M0 22 C70 0 140 6 220 30 C300 52 360 40 410 22 L410 170 L0 170 Z" fill="url(#waveFrontFill)"/>
    </svg>
    <div class="corner corner--bottom-right"></div>
  </section>

  <section class="card card--back">
    <div class="corner corner--top-left"></div>
    <div class="person">
      <p class="person__name">Derek Vellmore - CAT(C), CK, CSCS,</p>
      <p class="person__title">Certified Athletic Therapist</p>
      <p class="person__title">Strength and Conditioning Specialist</p>
    </div>
    <ul class="contact">
      <li>phone: 1234 5678</li>
      <li>email: derek@vellmoreathletics.example</li>
      <li>web: www.vellmoreathletics.example</li>
    </ul>
    <svg class="wave" viewBox="0 0 410 170" role="img" aria-label="Soft dotted halftone wave texture along the bottom of the card">
      <defs>
        <linearGradient id="waveBackFill" x1="0" y1="0" x2="0" y2="1">
          <stop offset="0" stop-color="var(--wave-light)"/>
          <stop offset="0.45" stop-color="var(--wave-mid)"/>
          <stop offset="1" stop-color="var(--wave-dark)"/>
        </linearGradient>
      </defs>
      <path d="M0 22 C70 0 140 6 220 30 C300 52 360 40 410 22 L410 170 L0 170 Z" fill="url(#waveBackFill)"/>
    </svg>
    <div class="corner corner--bottom-right"></div>
  </section>
</main>
</body>
</html>
```